Company or website name
- The Quillstone Movers and Storage
- Links to the website
- Quillstonehauling.com
- Describe your company and organization and target audience
- Residential and commercial moving and relocation service that needs a website redesign.
- The design should have the following
- I NEED THE WEBSITE TO BE SIMPLE AND STRAIGHT TO THE POINT...MAIN CONCERN IS THAT THEY FILL OUT INFORMATION TO GET QUOTE. SITE EXAMPLE THAT I LIKE IS ( WWW.MYPELDRAN.COM) https://www.orvikhaulage.com/

```html
<!DOCTYPE html>
<html lang="en">
<head>
<meta charset="utf-8">
<title>Quillstone Movers and Storage – Get Moved</title>
<link href="https://fonts.googleapis.com/css2?family=Roboto:ital,wght@0,400;0,500;0,700;1,400&family=Roboto+Condensed:wght@700&display=swap" rel="stylesheet">
<style>
  :root{
    --bar:#1f3714;
    --green:#6f9740;
    --green-soft:#86ad4e;
    --tab-off:#ececec;
    --tab-off-text:#b9b9b9;
    --text:#222;
    --error:#e4141b;
    --border:#9a9a9a;
    --white:#fff;
  }
  *{box-sizing:border-box;margin:0;padding:0}
  html,body{width:1200px;height:626px;overflow:hidden;background:var(--white)}
  body{position:relative;font-family:"Roboto",sans-serif;color:var(--text)}

  .announcement{position:absolute;left:0;top:0;width:1200px;height:57px;background:var(--bar);color:var(--white)}
  .announcement__icon{position:absolute;left:216px;top:15px}
  .announcement__text{position:absolute;left:262px;top:17px;font-size:17px;line-height:20px}
  .announcement__text strong{font-weight:700}
  .announcement__btn{position:absolute;left:805px;top:10px;width:179px;height:37px;background:var(--white);color:#1b1b1b;border-radius:3px;font-size:14px;font-weight:500;display:flex;align-items:center;justify-content:center;gap:4px}
  .announcement__close{position:absolute;left:1158px;top:20px;font-size:14px;font-weight:500}

  .hero{position:absolute;left:0;top:57px;width:676px;height:569px;overflow:hidden;color:var(--white)}
  .hero__photo{position:absolute;inset:0;background:linear-gradient(160deg,#8db65a 0%,#7aa545 45%,#5f8a35 75%,#7aa246 100%)}
  .brand{position:absolute;left:75px;top:24px;display:flex;align-items:center;gap:8px}
  .brand__mark{width:20px;height:20px;background:var(--white)}
  .brand__name{font-size:26px;font-weight:700;letter-spacing:2px}
  .nav{position:absolute;left:345px;top:47px;display:flex;font-size:12.5px;letter-spacing:.2px}
  .nav a{color:var(--white);text-decoration:none}
  .nav .services{margin-right:14px;display:flex;align-items:center;gap:4px}
  .nav .faqs{margin-right:29px}
  .nav .blog{margin-right:30px}
  .headline{position:absolute;left:161px;top:247px;width:357px;height:65px;border-top:1px solid rgba(255,255,255,.85);border-bottom:1px solid rgba(255,255,255,.85);font-family:"Roboto Condensed",sans-serif;font-weight:700;font-size:62px;line-height:63px;white-space:nowrap;letter-spacing:-.5px}

  .quote{position:absolute;left:676px;top:57px;width:524px;height:569px}
  .tab{position:absolute;top:23px;width:138px;height:93px;border:1px solid #dcdcdc;background:var(--tab-off);color:var(--tab-off-text);display:flex;flex-direction:column;align-items:center;justify-content:flex-end;padding-bottom:16px;font-size:14px;font-weight:500;gap:8px}
  .tab--active{background:var(--green);border-color:var(--green);color:var(--white)}
  .tab--res{left:24px}.tab--office{left:168px}.tab--reloc{left:312px}

  .label{position:absolute;font-size:12px}
  .field{position:absolute;height:40px;width:209px;border:1px solid var(--border);background:var(--white);font-size:11px;padding-left:13px;display:flex;align-items:center}
  .col-a{left:24px}.col-b{left:241px}
  .error{position:absolute;font-size:10.5px;color:var(--error)}
  .hint{position:absolute;font-size:10px}
  .btn{position:absolute;top:464px;width:209px;height:40px;font-size:16px;font-weight:700;display:flex;align-items:center;justify-content:center}
  .btn--quote{left:24px;background:var(--green);color:var(--white)}
  .btn--reserve{left:241px;border:2px solid var(--green);color:var(--green);background:var(--white)}
  .footnote{position:absolute;left:0;top:531px;width:596px;text-align:center;font-size:10px;font-style:italic;color:#333}
</style>
</head>
<body>
  <header class="announcement">
    <svg class="announcement__icon" width="31" height="24" viewBox="0 0 31 24" fill="none" stroke="#fff" stroke-width="1.5">
      <path d="M2 8h6l10-6v18L8 14H2z"/><path d="M5 14l2 8h4l-2-8"/><path d="M22 11h6M22 5l5-3M22 17l5 3"/>
    </svg>
    <p class="announcement__text"><strong>ANNOUNCEMENT:</strong> Please read our latest updates on COVID-19</p>
    <div class="announcement__btn">Read More
      <svg width="14" height="8" viewBox="0 0 14 8"><path d="M0 4h12M9 1l3 3-3 3" stroke="#1b1b1b" stroke-width="1.6" fill="none"/></svg>
    </div>
    <span class="announcement__close">X</span>
  </header>

  <section class="hero">
    <div class="hero__photo" role="img" aria-label="Moving truck with trailer under a cloudy sky, tinted green"></div>
    <div class="brand"><span class="brand__mark"></span><span class="brand__name">QUILLSTONE</span></div>
    <nav class="nav">
      <a class="services" href="#">SERVICES
        <svg width="9" height="6" viewBox="0 0 9 6"><path d="M1 1l3.5 3.5L8 1" stroke="#fff" stroke-width="1.4" fill="none"/></svg></a>
      <a class="faqs" href="#">FAQS</a>
      <a class="blog" href="#">BLOG</a>
      <a href="#">CONTACT</a>
    </nav>
    <h1 class="headline">GET MOVED.</h1>
  </section>

  <section class="quote">
    <div class="tab tab--active tab--res">
      <svg width="34" height="32" viewBox="0 0 34 32" fill="none" stroke="#fff" stroke-width="1.6"><path d="M2 16L17 2l15 14"/><path d="M6 13v17h22V13"/><path d="M13 30V20h8v10"/></svg>
      Residential
    </div>
    <div class="tab tab--office">
      <svg width="40" height="32" viewBox="0 0 40 32" fill="none" stroke="#b9b9b9" stroke-width="1.4"><rect x="2" y="4" width="20" height="27"/><rect x="22" y="12" width="16" height="19"/><path d="M2 4h20M4 1h16"/><path d="M6 9h3v3H6zM13 9h3v3h-3zM6 16h3v3H6zM13 16h3v3h-3zM26 17h3v3h-3zM31 17h3v3h-3zM26 23h3v3h-3zM31 23h3v3h-3z"/></svg>
      Office
    </div>
    <div class="tab tab--reloc">
      <svg width="56" height="32" viewBox="0 0 56 32" fill="none" stroke="#b9b9b9" stroke-width="1.4"><path d="M2 30l10-14h32l10 14z"/><path d="M10 16c0-6 8-6 8 0 0 4-4 8-4 8s-4-4-4-8z"/><path d="M37 6c0-5 7-5 7 0 0 3-3.5 7-3.5 7S37 9 37 6z"/><path d="M14 24c8 0 10-4 18-4s8-4 9-7" stroke-dasharray="3 2"/></svg>
      Relocation
    </div>

    <span class="label col-a" style="top:154px">I am moving from... *</span>
    <span class="label col-b" style="top:154px">I am moving to...*</span>
    <div class="field col-a" style="top:173px">Zip Code</div>
    <div class="field col-b" style="top:173px">Zip Code</div>
    <span class="error col-a" style="top:217px">This field is required.</span>

    <span class="label col-a" style="top:249px">Moving Date*</span>
    <span class="label col-b" style="top:253px">Your Full Name (First and Last) *</span>
    <div class="field col-a" style="top:273px"></div>
    <div class="field col-b" style="top:273px"></div>
    <span class="hint col-a" style="top:319px">Date Format: MM slash DD slash YYYY</span>
    <span class="error col-b" style="top:323px">This field is required.</span>
    <span class="error col-a" style="top:336px">This field is required.</span>

    <span class="label col-a" style="top:367px">Your E-Mail Address *</span>
    <span class="label col-b" style="top:367px">Your Phone Number *</span>
    <div class="field col-a" style="top:391px"></div>
    <div class="field col-b" style="top:391px"></div>
    <span class="error col-a" style="top:438px">This field is required.</span>
    <span class="error col-b" style="top:438px">This field is required.</span>

    <div class="btn btn--quote">FREE QUOTE</div>
    <div class="btn btn--reserve">MAKE A RESERVATION</div>
    <p class="footnote">A Peldran Moving Solutions agent will be e-mailing you a quote in 24 hours or less</p>
  </section>
</body>
</html>
```